Dalwin Tasker Construction LLC

I like to have a business card the is unique, very professional and the it will projected the best first impression of me and my company

Target Market(s)

Remodeling, new constitution

Industry/Entity Type

Business

Font styles to use
Script

Requirements
Must have
• My company name email and phone number
Nice to have
• A logo maybe

```html
<!DOCTYPE html>
<html lang="en">
<head>
<meta charset="utf-8">
<title>Dalwin Tasker Construction LLC – Business Card</title>
<link rel="stylesheet" href="https://fonts.googleapis.com/css2?family=Quicksand:wght@600&family=Lato:wght@400;700;900&display=swap">
<style>
  :root {
    --orange: #f29100;
    --charcoal: #33302e;
    --slate: #6e6e6e;
    --ink: #3a3a3a;
    --paper: #ffffff;
    --backdrop: #e9e7e7;
  }
  * { box-sizing: border-box; margin: 0; padding: 0; }
  html, body {
    width: 1200px;
    height: 863px;
    overflow: hidden;
    background: var(--backdrop);
  }
  .stage {
    width: 1200px;
    height: 863px;
    display: flex;
    justify-content: center;
    align-items: center;
    gap: 80px;
  }
  .card {
    position: relative;
    width: 340px;
    height: 580px;
    background: var(--paper);
    box-shadow: 0 6px 18px rgba(0,0,0,0.18);
    display: flex;
    flex-direction: column;
    overflow: hidden;
  }
  .card__top-band { height: 62px; background: var(--orange); flex: none; }
  .card__bottom-band { height: 82px; background: var(--charcoal); flex: none; margin-top: auto; }
  .card__body {
    flex: 1;
    display: flex;
    flex-direction: column;
    align-items: center;
  }
  .card--front .card__body { justify-content: center; }

  .company-name {
    font-family: "Quicksand", sans-serif;
    font-weight: 600;
    color: var(--orange);
    text-align: center;
    line-height: 1.1;
  }
  .card--front .company-name { font-size: 34px; }
  .card--back .company-name { font-size: 24px; margin-top: 70px; }

  .name-plate {
    margin-top: 22px;
    width: 82%;
    background: var(--slate);
    color: var(--paper);
    text-align: center;
    padding: 9px 0 8px;
    font-family: "Lato", sans-serif;
  }
  .name-plate__name { font-size: 20px; letter-spacing: 0.5px; line-height: 1; }
  .name-plate__name strong { font-weight: 900; }
  .name-plate__title { font-size: 10px; font-weight: 700; letter-spacing: 0.5px; margin-top: 3px; }

  .contact-list { width: 82%; margin-top: 22px; list-style: none; }
  .contact-row {
    display: flex;
    align-items: center;
    gap: 14px;
    padding-bottom: 6px;
    margin-bottom: 14px;
    border-bottom: 2px solid var(--orange);
  }
  .contact-row__icon {
    width: 34px; height: 34px;
    background: var(--orange);
    display: flex; align-items: center; justify-content: center;
    flex: none;
  }
  .contact-row__text {
    font-family: "Lato", sans-serif;
    font-size: 12px;
    color: var(--ink);
    line-height: 1.2;
  }
</style>
</head>
<body>
<main class="stage">
  <article class="card card--front">
    <div class="card__top-band"></div>
    <div class="card__body">
      <h1 class="company-name">Dalwin Tasker<br>Construction LLC</h1>
    </div>
    <div class="card__bottom-band"></div>
  </article>

  <article class="card card--back">
    <div class="card__top-band"></div>
    <div class="card__body">
      <h2 class="company-name">Dalwin Tasker<br>Construction LLC</h2>
      <div class="name-plate">
        <div class="name-plate__name"><strong>JOHN</strong> DOE</div>
        <div class="name-plate__title">DIRECTOR</div>
      </div>
      <ul class="contact-list">
        <li class="contact-row">
          <span class="contact-row__icon">
            <svg width="18" height="18" viewBox="0 0 24 24" aria-hidden="true">
              <path fill="#fff" d="M6.6 10.8a15.1 15.1 0 0 0 6.6 6.6l2.2-2.2c.3-.3.7-.4 1-.2 1.1.4 2.3.6 3.6.6.6 0 1 .4 1 1V20c0 .6-.4 1-1 1A17 17 0 0 1 3 4c0-.6.4-1 1-1h3.5c.6 0 1 .4 1 1 0 1.3.2 2.5.6 3.6.1.3 0 .7-.2 1z"/>
            </svg>
          </span>
          <span class="contact-row__text">+ 000 - 1234 - 5678<br>+ 000 - 9876 - 5432</span>
        </li>
        <li class="contact-row">
          <span class="contact-row__icon">
            <svg width="18" height="18" viewBox="0 0 24 24" aria-hidden="true">
              <rect x="2" y="3" width="20" height="14" rx="1" fill="none" stroke="#fff" stroke-width="2"/>
              <rect x="8" y="19" width="8" height="2" fill="#fff"/>
            </svg>
          </span>
          <span class="contact-row__text">email@sitename.com<br>www.sitename.com</span>
        </li>
      </ul>
    </div>
    <div class="card__bottom-band"></div>
  </article>
</main>
</body>
</html>
```